Web Design Project

Hello, my name is Reid Palmquist. I own and operate Corvid Printworks a small printing business in Long Island, NY. I specialize in the reproduction of artwork.
My current website is geared more for the stiff clients I have. This new site will be the bastard step child of the current site.
The printing process is call giclee, which basically means that the prints are done with archival inks and papers. Most of my customers are in the tattoo industry and low-brow art community. I am looking for a slick website that I can showcase some of the work I have done as well as a place for artists to get information on my pricing and what it is that I do. I want the ability to have admin capabilities so I can make changes to the site at will (upload pics, change info ect.). I would also like to link it to a wordpress blog or have a blog built into it directly. Also have it linked to Chatter, Facepage, instagram and other outside links as well. I have a logo already designed that is very much a part of my brand. This logo and other info I provide will set the tone for what I am looking for.

Target Market(s)

Artistis

Industry/Entity Type

Printing

Requirements
Must have
• I want the ability to have admin capabilities so I can make changes to the site at will (upload pics, change info ect.).
Nice to have
• I would want this to also have a gallery for people to see the work I have done in the past.

I can also provide high-res files of my logo.

```html
<!DOCTYPE html>
<html lang="en">
<head>
<meta charset="utf-8">
<title>Corvid Printworks</title>
<link rel="stylesheet" href="https://fonts.googleapis.com/css2?family=Cinzel:wght@400;700&family=Goudy+Bookletter+1911&family=Open+Sans:wght@400;600;700&family=Tinos:ital@0;1&display=swap">
<style>
:root{
  --page:#231d19;
  --page-deep:#1a1512;
  --panel:#141110;
  --cream:#efe9dc;
  --parchment:#e7dcc4;
  --nav-top:#fbeedd;
  --nav-bottom:#f1d6b3;
  --orange:#f29b1c;
  --gold:#c9a56a;
  --red:#c62121;
  --red-dark:#8e1515;
  --brown:#7a4a1c;
  --text-light:#e8e1d5;
  --text-mute:#8d857b;
  --ink:#2b2119;
}
*{box-sizing:border-box;margin:0;padding:0}
html,body{width:998px;height:1200px;overflow:hidden}
body{background:var(--page);font-family:"Open Sans",Arial,sans-serif;color:var(--text-light);position:relative}
.abs{position:absolute}

.topbar .call{left:120px;top:4px;font-size:12px;color:#fff}
.topbar .call b{color:var(--orange);font-weight:400;font-size:15px}
.login-tab{left:846px;top:5px;width:35px;height:19px;background:linear-gradient(#c98a3a,#8c5616);border-radius:3px 3px 0 0;font-size:10px;color:#fff;text-align:center;line-height:19px}

.nav{left:0;top:24px;width:998px;height:38px;background:linear-gradient(var(--nav-top),var(--nav-bottom));border-bottom:1px solid #d7b58a}
.nav ul{list-style:none;position:absolute;left:117px;top:4px;display:flex;font-family:"Tinos",serif;font-size:13px;color:#3a2a1c}
.nav li{padding:0 7px;line-height:28px}
.nav li.active{background:linear-gradient(#f0a62a,#c56d05);color:#fff;border-radius:3px;padding:0 8px}
.send{left:781px;top:4px;width:100px;height:30px;background:linear-gradient(#e23a2c,#b11616);border-radius:4px;color:#fff;font-size:14px;text-align:center;line-height:30px;letter-spacing:.3px}

.hero{left:0;top:62px;width:998px;height:351px;background:#ece7dc}
.logo-area{left:120px;top:104px;width:198px;height:226px;background:linear-gradient(#e5d6b2,#d6bd86);border:2px solid #3a2a1c;display:flex;align-items:center;justify-content:center;gap:8px}
.logo-area .mark{width:14px;height:14px;background:var(--red)}
.logo-area span{font-family:"Cinzel",serif;font-weight:700;font-size:15px;color:var(--ink)}
.hero-photo{left:320px;top:62px;width:255px;height:351px;background:linear-gradient(160deg,#5d7da3 0%,#3a3430 45%,#c9b9a3 100%)}
.hero-copy{left:575px;top:62px;width:302px;height:351px;background:linear-gradient(#e6dcc5,#d8c8a8);font-family:"Cinzel",serif;color:var(--ink);text-align:center}
.hero-copy p{position:absolute;left:0;width:302px;white-space:nowrap}
.hero-copy .script{font-family:"Tinos",serif;font-style:italic}
.hero-copy .headline{font-size:21px;line-height:27px;letter-spacing:-.4px}
.hero-copy .rule{position:absolute;left:8px;width:286px;height:1px;background:var(--ink)}
.hero-edge{left:0;top:413px;width:998px;height:6px;background:linear-gradient(#8a5a26,#4a2c10)}
.badge{left:428px;top:325px;width:150px;height:120px}

.features .tile{top:479px;width:232px;height:45px;background:var(--panel);border-radius:4px;color:var(--orange);font-size:14px;text-align:center;padding-top:21px}
.features .halo{top:430px;width:80px;height:80px;border-radius:50%;border:1px dashed #4a3f36}
.features svg{z-index:2}

.welcome h2{font-family:"Goudy Bookletter 1911",serif;font-weight:400}
.welcome .small{left:118px;top:541px;font-size:19px;color:var(--gold)}
.welcome .big{left:117px;top:558px;font-size:27px;color:var(--cream)}
.welcome p{left:117px;top:604px;width:266px;font-size:8.2px;line-height:12.4px;color:var(--text-mute)}
.btn-red{background:linear-gradient(#d8302a,#a51616);color:#fff;font-size:9px;border-radius:3px;text-align:center;line-height:17px;height:17px}

.news h2{left:407px;top:556px;font-family:"Goudy Bookletter 1911",serif;font-weight:400;font-size:26px;color:var(--parchment)}
.news .dots{left:405px;top:596px;width:267px;border-top:1px dotted #5a5048}
.news .item{left:405px;width:267px}
.news .item h4{font-size:9px;font-weight:700;color:#fff}
.news .item p{font-size:8.2px;line-height:12px;color:var(--text-mute)}

.signin{left:686px;top:549px;width:196px;height:167px}
.signin .tab{position:absolute;left:0;top:0;width:145px;height:34px;background:var(--red);border-radius:4px 4px 0 0;color:#fff;font-size:13px;padding:9px 10px}
.signin .box{position:absolute;left:0;top:33px;width:196px;height:134px;background:#fbfaf8;border-radius:0 4px 4px 4px}
.signin .field{position:absolute;left:10px;width:176px;height:27px;background:linear-gradient(#ddd4ca,#efe9e3);border-radius:4px;font-size:9px;color:#5a4f47;padding:8px}
.signin .go{position:absolute;left:11px;top:82px;width:56px;height:23px;background:linear-gradient(#c42a22,#8d1212);border-radius:4px;color:#fff;font-size:12px;text-align:center;line-height:23px}
.signin .forgot{position:absolute;left:11px;top:112px;font-size:8.6px;color:var(--red-dark)}

.hours{left:686px;top:738px;width:196px;height:70px;border:1px dotted #4a4038}
.hours h3{position:absolute;left:0;width:194px;top:3px;text-align:center;font-weight:400;font-size:18px;color:var(--orange)}
.hours .day{position:absolute;top:30px;height:32px;background:var(--panel);font-size:8.4px;padding:3px 0 0 10px;color:#fff}
.hours .day b{color:var(--orange);display:block}

.lower{left:117px;top:824px;width:562px;height:152px;background:linear-gradient(#f0ece2,#e5e0d3);border-radius:5px}
.lower h3{position:absolute;top:8px;font-weight:400;font-size:18px;color:var(--red)}
.lower .line{position:absolute;top:34px;height:1px;border-top:1px dotted #b8ad9b}
.tip-title{left:10px;top:43px;font-size:9.5px;font-weight:700;color:var(--red)}
.tip-body{left:10px;top:56px;width:262px;font-size:9px;line-height:12.6px;font-weight:600;color:#3d3530}
.services{left:290px;top:41px;list-style:none;font-size:9.5px;color:#2f2925}
.services li{line-height:17.2px;padding-left:11px;position:relative}
.services li::before{content:"";position:absolute;left:0;top:6px;border-left:4px solid #9a9188;border-top:3px solid transparent;border-bottom:3px solid transparent}
.lower .more{width:77px;height:21px;line-height:21px;font-size:9.5px;font-weight:700;letter-spacing:.4px}

.map-label{left:687px;top:822px;font-size:13px;color:var(--parchment)}
.map{left:687px;top:848px;width:194px;height:128px;background:linear-gradient(#f3f1ec,#dcd8cf);border:3px solid #3b3531}

.footer-rule{left:0;top:1002px;width:998px;border-top:1px dashed #3e352e}
.foot h3{font-weight:400;font-size:15.5px;color:var(--orange)}
.foot .sub{font-size:8.5px;color:#b9b1a6;font-weight:600}
.input{background:#2f2824;border-radius:3px;font-size:9.5px;font-style:italic;color:#c8bfb4;padding:6px 8px}
.social{left:440px;list-style:none;font-size:8.5px;color:#b9b1a6}
.social li{height:32px;display:flex;align-items:center;gap:9px}
.social .ico{width:20px;height:20px;border-radius:3px}
.links{left:627px;top:1042px;list-style:none;font-size:8.4px;color:#b9b1a6;width:100px}
.links li{height:18px;line-height:18px;border-bottom:1px solid #2f2824}
.address{left:741px;top:1013px;width:141px;height:152px;background:var(--page-deep);border-radius:3px;padding:5px 9px}
.address h3{font-weight:400;font-size:15.5px;color:var(--orange);line-height:18px}
.address p{font-size:8.4px;line-height:12px;color:#b9b1a6;margin-top:7px}
.copy{left:686px;top:1183px;font-size:8.4px;color:#b9b1a6}
.copy b{color:var(--orange);font-weight:400}
</style>
</head>
<body>

<header class="topbar">
  <div class="abs call">Call us on: <b>555.210.4400</b></div>
  <div class="abs login-tab">Login</div>
</header>

<nav class="abs nav">
  <ul>
    <li class="active">HOME</li><li>OUR HISTORY</li><li>DOCUMENT SERVICES</li><li>TECH SPECS</li><li>DIGITAL TIPS</li><li>NEWS</li><li>CONTACT US</li>
  </ul>
  <div class="abs send">SEAD A FILE</div>
</nav>

<section class="abs hero"></section>
<div class="abs logo-area"><i class="mark"></i><span>Corvid Printworks</span></div>
<div class="abs hero-photo" role="img" aria-label="Photo of two printers checking a fresh large-format print at the press"></div>
<div class="abs hero-copy">
  <p style="top:18px;font-size:15px">CORVID PRINTWORKS</p>
  <p class="script" style="top:37px;font-size:13px">creating high quality</p>
  <div class="rule" style="top:60px"></div>
  <p class="headline" style="top:67px">FINE ART GICLÉE &amp;<br>DIGITAL REPRODUCTIONS</p>
  <div class="rule" style="top:125px"></div>
  <p class="script" style="top:132px;font-size:14px">produced on</p>
  <p style="top:153px;font-size:17px;line-height:20px">100% COTTON RAG<br>ACID FREE PAPER</p>
  <p style="top:198px;font-family:'Tinos',serif;font-size:15px">Using 100+ Year Archival Pigments</p>
  <div class="rule" style="top:228px"></div>
  <p class="script" style="top:234px;font-size:14px">also offering</p>
  <p style="top:255px;font-size:16px;line-height:20px;font-weight:700">FLASH REPRODUCTIONS<br>CANVAS BANNERS<br>SKETCH BOOKS</p>
  <p class="script" style="top:319px;font-size:18px">555-210-4400</p>
</div>
<div class="abs hero-edge"></div>
<svg class="abs badge" viewBox="0 0 150 120" aria-hidden="true">
  <polygon fill="#c07a24" stroke="#7a4a1c" points="75,0 84,18 102,8 104,28 124,24 118,43 140,46 128,62 146,74 122,78 75,118 28,78 4,74 22,62 10,46 32,43 26,24 46,28 48,8 66,18"/>
  <text x="75" y="57" text-anchor="middle" font-family="Cinzel,serif" font-weight="700" font-size="17" fill="#1c140e">FTP</text>
  <text x="75" y="77" text-anchor="middle" font-family="Cinzel,serif" font-weight="700" font-size="17" fill="#1c140e">/E-Order</text>
</svg>

<section class="features">
  <div class="abs halo" style="left:218px"></div>
  <div class="abs halo" style="left:459px"></div>
  <div class="abs halo" style="left:700px"></div>
  <div class="abs tile" style="left:142px">Upload Your Own Digital Files</div>
  <div class="abs tile" style="left:383px">Check Your Job Status</div>
  <div class="abs tile" style="left:624px">Reliable &amp; Secure</div>
  <svg class="abs" style="left:231px;top:444px" width="56" height="52" viewBox="0 0 56 52" aria-hidden="true">
    <path d="M4 26h48v22H4z" fill="#d8d8d8"/><path d="M0 22h56l-4 6H4z" fill="#f2f2f2"/>
    <path d="M28 2l14 14h-8v12H22V16h-8z" fill="#4fb33c"/>
  </svg>
  <svg class="abs" style="left:470px;top:446px" width="54" height="50" viewBox="0 0 54 50" aria-hidden="true">
    <path d="M8 4l30-2 6 38-30 4z" fill="#fafafa" stroke="#bbb"/>
    <path d="M14 12l3 3 5-6M14 22l3 3 5-6M14 32l3 3 5-6" stroke="#c62121" stroke-width="2" fill="none"/>
    <path d="M26 14h12M26 24h12M26 34h12" stroke="#999"/>
    <path d="M30 44l18-18 3 3-18 18-5 1z" fill="#333"/>
  </svg>
  <svg class="abs" style="left:710px;top:446px" width="64" height="52" viewBox="0 0 64 52" aria-hidden="true">
    <path d="M2 20l30-18 30 18-30 30z" fill="#2f6fc8"/><path d="M8 20l24-14 24 14-24 24z" fill="#5a9ae6"/>
  </svg>
</section>

<section class="welcome">
  <h2 class="abs small">Welcome to</h2>
  <h2 class="abs big">Corvid Printworks</h2>
  <p class="abs">The Northline Print Network is the largest and only fully certified network of reprographic companies in the USA. Their 220 members represent over 6000 employees, 1,000 delivery vehicles, 800 wide format printers, and cover 170 cities. The Network anticipates a myriad of new digital opportunities with the evolution of technology and increasing connectivity. As the architectural, engineering and construction (AEC) community look to digital solutions for their printing needs, the mission of the Northline Print Network will be to find those opportunities and make them available to our members and their clients. Headquarter in Harlow City, Ohio; the Northline Print Network was founded in May of 1999 by Eastgate Plan Works.</p>
  <div class="abs btn-red" style="left:117px;top:775px;width:58px">Read More</div>
</section>

<section class="news">
  <h2 class="abs">What's New ?</h2>
  <div class="abs dots"></div>
  <div class="abs item" style="top:604px"><h4>Introducing The Vantor Mono 1050</h4><p>The ideal solution for samll format B/W copying, printing and scanning</p></div>
  <div class="abs item" style="top:649px"><h4>Introducing The Lumen CS4050</h4><p>The ideal solution for large format color scanning, copying and archiving</p></div>
  <div class="abs item" style="top:692px"><h4>Introducing The Vantor Color Force 8050</h4><p>The ideal solution for Small format color printing, copying and scanning</p></div>
  <div class="abs item" style="top:736px"><h4>Summer Special</h4><p>Turn your photos into full size color posters</p></div>
  <div class="abs btn-red" style="left:405px;top:775px;width:58px">Read More</div>
</section>

<aside class="abs signin">
  <div class="tab">ONLINE SIGN IN</div>
  <svg style="position:absolute;left:140px;top:0" width="30" height="34" aria-hidden="true"><path d="M0 0h6l22 34H0z" fill="#c62121"/></svg>
  <div class="box">
    <div class="field" style="top:10px">Username</div>
    <div class="field" style="top:49px">Password</div>
    <div class="go">Login</div>
    <div class="forgot">Forgot User Name Or Password?</div>
  </div>
</aside>

<aside class="abs hours">
  <h3>Store Hours</h3>
  <div class="day" style="left:4px;width:88px"><b>MON-FRI</b>9:00 AM - 5:00 PM</div>
  <div class="day" style="left:97px;width:94px"><b>SAT</b>10:00 AM - 3:00 PM</div>
</aside>

<section class="abs lower">
  <h3 style="left:10px">Digital Tips</h3>
  <div class="line" style="left:10px;width:256px"></div>
  <div class="abs tip-title">What is Digital Printing?</div>
  <p class="abs tip-body">Digital printing means using an electronic file (on a disk or similar medium) to produce hard-copy originals of your document, rather than placing your original on the copier and making reproductions (the latter is called analog printing).</p>
  <div class="abs btn-red more" style="left:187px;top:125px">Read More ›</div>
  <h3 style="left:289px">Document Services</h3>
  <div class="line" style="left:289px;width:265px"></div>
  <ul class="abs services"><li>Cad Graphics</li><li>Digital Color</li><li>Small Format B&amp;W</li><li>Vectorization</li><li>Document Finishing</li></ul>
  <div class="abs btn-red more" style="left:475px;top:125px">Read More ›</div>
</section>

<div class="abs map-label">Map</div>
<div class="abs map" role="img" aria-label="Street map showing the shop location"></div>

<div class="abs footer-rule"></div>

<footer class="foot">
  <h3 class="abs" style="left:117px;top:1015px">Get in Touch</h3>
  <div class="abs sub" style="left:118px;top:1035px">Please fill in the form below.</div>
  <div class="abs input" style="left:117px;top:1057px;width:147px;height:24px">Your Full Name</div>
  <div class="abs input" style="left:272px;top:1057px;width:147px;height:24px">Your Email Address</div>
  <div class="abs input" style="left:117px;top:1090px;width:302px;height:78px">Your Message</div>
  <div class="abs btn-red" style="left:118px;top:1177px;width:94px;height:23px;line-height:23px;font-size:11px;font-weight:700">Submit Form</div>

  <h3 class="abs" style="left:440px;top:1015px">What to keep in touch?</h3>
  <ul class="abs social" style="top:1043px">
    <li><i class="ico" style="background:#4fb0e6"></i>Follow us on Chatter</li>
    <li><i class="ico" style="background:#3b5b9a"></i>Like us on Facepage</li>
    <li><svg class="ico" viewBox="0 0 20 20" style="background:#f08a1c"><circle cx="5" cy="15" r="2" fill="#fff"/><path d="M3 9a8 8 0 018 8M3 4a13 13 0 0113 13" stroke="#fff" stroke-width="2.2" fill="none"/></svg>Subscribe to our Rss feed</li>
    <li><svg class="ico" viewBox="0 0 20 20" style="background:#d32a1e"><rect x="4" y="6" width="12" height="9" fill="none" stroke="#fff" stroke-width="1.5"/><path d="M4 6l6 5 6-5" stroke="#fff" stroke-width="1.5" fill="none"/></svg>Contact us by email</li>
  </ul>

  <h3 class="abs" style="left:627px;top:1015px">Site links</h3>
  <ul class="abs links"><li>Home</li><li>Our History</li><li>Document Services</li><li>Tech Specs</li><li>Digital Tips</li><li>News</li><li>Contact US</li></ul>

  <div class="abs address">
    <h3>Corvid<br>Printworks</h3>
    <p>48 Kestrel Road<br>Suite One<br>Millbrook, New York 11790</p>
    <p>Phone:<br>555.210.4400<br>fax.555.7699</p>
  </div>

  <div class="abs copy">© 2011 <b>Corvid Printworks</b>. All Rights Reserved.</div>
</footer>

</body>
</html>
```